Quorvantelline.com

I need a site that I can sell dewatering equipment to the construction industry.
Ie, pipes fittings pumps and other such things needed to remove the groundwater on construction sites. Here in Florida, it’s needed almost everywhere seeing we are at sea level.
I want to be able to sell these products on the site and receive

Coded - Design and coding required

1 page

```html
<!DOCTYPE html>
<html lang="en">
<head>
<meta charset="utf-8">
<title>Quorvantelline Layout</title>
<link href="https://fonts.googleapis.com/css2?family=Lato:wght@300;400;700;900&display=swap" rel="stylesheet">
<style>
:root{
  --board-blue:#4f82b5;
  --board-grey:#4a4a4a;
  --navy:#0d2c5e;
  --navy-soft:#1f4470;
  --yellow:#f2b91a;
  --yellow-deep:#e0a812;
  --light:#f2f2f2;
  --tile:#e2e2e2;
  --text:#555;
  --muted:#888;
  --footer:#2f2f2f;
  --footer-base:#262626;
  --white:#fff;
}
*{box-sizing:border-box;margin:0;padding:0}
html,body{width:1200px;height:2347px;overflow:hidden}
body{font-family:'Lato',sans-serif;color:var(--text);position:relative;
  background:linear-gradient(to bottom right,var(--board-blue) 0,var(--board-blue) 100%);}
.board-shade{position:absolute;left:0;top:0;width:1200px;height:2347px}
.board-title{position:absolute;top:50px;left:0;width:1200px;text-align:center;color:var(--white);font-weight:700;font-size:37px;letter-spacing:-.3px}
.site{position:absolute;left:111px;top:132px;width:978px;background:var(--white)}
.inner{width:734px;margin:0 auto;position:relative;height:100%}

/* header */
.topbar{height:43px;background:var(--navy)}
.brand{position:absolute;left:0;top:12px;display:flex;align-items:center;gap:8px;color:var(--white);font-weight:700;font-size:13px;letter-spacing:-.2px}
.brand-mark{width:12px;height:12px;background:var(--yellow)}
.contact-strip{position:absolute;right:0;top:10px;display:flex;gap:24px}
.contact-item{display:flex;align-items:center;gap:9px}
.contact-icon{width:20px;height:16px;border:1px solid var(--yellow);display:flex;align-items:center;justify-content:center}
.contact-label{font-size:8px;line-height:10px;color:var(--yellow)}
.contact-value{font-size:8px;line-height:10px;color:#d5dbe6}
.navbar{height:32px;background:var(--yellow)}
.nav-links{display:flex;height:32px;list-style:none}
.nav-links li{font-size:8.5px;color:var(--white);padding:0 17px;display:flex;align-items:center;border-right:1px solid rgba(255,255,255,.35)}
.nav-links li:last-child{border-right:0}
.nav-links li.active{background:var(--yellow-deep)}
.social{position:absolute;right:0;top:0;height:32px;display:flex;align-items:center;gap:6px;font-size:7.5px;font-weight:700;color:var(--white)}

/* hero */
.hero{height:353px;position:relative;background:radial-gradient(ellipse at 50% 60%,#5f6b6e 0,#3a3a34 45%,#1c1b17 100%)}
.hero-caption{position:absolute;left:50%;top:134px;transform:translateX(-50%);width:349px;height:67px;border:1px solid rgba(255,255,255,.55);background:rgba(0,0,0,.2);text-align:center;padding-top:8px}
.hero-caption h1{color:var(--yellow);font-size:29px;font-weight:700;line-height:32px;letter-spacing:-.3px}
.hero-caption p{color:var(--white);font-size:13px;margin-top:1px}
.hero-dots{position:absolute;left:50%;transform:translateX(-50%);bottom:13px;display:flex;gap:3px}
.hero-dots span{width:8px;height:8px;border-radius:50%;border:1px solid var(--white)}
.hero-dots span.on{background:var(--yellow);border-color:var(--yellow)}

/* intro */
.intro{height:174px}
.intro-heading{position:absolute;left:0;top:40px;color:var(--navy);font-weight:900;font-size:32px;line-height:34px}
.intro-heading small{display:block;font-weight:400;font-size:24px;color:#555;line-height:30px;margin-top:2px}
.intro-copy{position:absolute;left:261px;top:42px;width:460px}
.intro-copy h2{font-weight:400;font-size:15px;color:#444}
.intro-copy p{font-size:8.5px;line-height:13px;color:var(--muted);margin-top:7px}
.btn{display:inline-block;background:var(--yellow);color:var(--white);font-size:8.5px;border-radius:7px;text-align:center}
.intro-copy .btn{width:105px;height:26px;line-height:26px;margin-top:20px}

/* sections */
.section-title{position:absolute;left:0;width:100%;text-align:center;font-weight:400;font-size:20px;color:#555}
.services{height:385px;background:var(--light)}
.services .section-title{top:42px}
.service-cards{position:absolute;top:107px;left:0;display:flex;gap:13px}
.service-card{width:236px;height:210px;background:var(--white);padding:6px;text-align:center}
.service-photo{height:128px}
.service-card h3{color:var(--yellow);font-size:10.5px;font-weight:400;margin-top:16px}
.service-card p{font-size:8.5px;line-height:12px;color:var(--muted);margin-top:3px;padding:0 25px}

.products{height:478px}
.products .section-title{top:61px}
.product-grid{position:absolute;top:126px;left:0;display:grid;grid-template-columns:238px 238px 238px;grid-template-rows:131px 131px;column-gap:10px;row-gap:6px}
.product-tile{background:var(--tile)}
.product-feature{grid-column:2;grid-row:1 / span 2;background:var(--navy-soft);padding:6px}
.product-feature-frame{border:1px solid rgba(255,255,255,.18);height:100%;text-align:center;color:var(--white);padding-top:93px}
.product-feature h3{font-size:14px;font-weight:400}
.product-feature p{font-size:8.5px;line-height:12.5px;color:#d5dcea;margin-top:4px;padding:0 30px}
.product-feature .btn{width:100px;height:23px;line-height:23px;border-radius:2px;margin-top:6px}

.stats{height:107px;background:var(--navy)}
.stat{position:absolute;top:33px;width:140px;margin-left:-70px;text-align:center;color:var(--white)}
.stat strong{display:block;font-size:32px;font-weight:700;line-height:32px}
.stat span{font-size:8px}

.trust{height:308px}
.trust h2{position:absolute;top:65px;font-size:20px;font-weight:400;color:#555}
.client-grid{position:absolute;top:113px;left:0;width:308px;height:124px;border:1px solid #e5e5e5;display:grid;grid-template-columns:repeat(3,1fr);grid-template-rows:1fr 1fr}
.client{border-right:1px solid #e5e5e5;border-bottom:1px solid #e5e5e5;display:flex;align-items:center;justify-content:center;gap:5px;font-size:11px;font-weight:700;color:var(--navy-soft)}
.client:nth-child(3n){border-right:0}
.client:nth-child(n+4){border-bottom:0}
.client i{width:9px;height:9px;border-radius:50%;background:var(--navy-soft)}
.testimonial{position:absolute;left:386px;top:113px;width:348px;height:124px;border:1px solid #e5e5e5}
.testimonial blockquote{font-size:8.5px;line-height:12.5px;color:var(--muted);padding:16px 30px 0 16px}
.testimonial blockquote b{color:var(--yellow);font-size:13px;margin-right:5px}
.testimonial-bar{position:absolute;left:-1px;right:-1px;bottom:-1px;height:36px;background:var(--yellow-deep)}
.avatar{position:absolute;left:17px;top:-12px;width:48px;height:48px;border-radius:50%;background:#cfd6df;border:2px solid var(--white)}
.testimonial-bar span{position:absolute;left:74px;top:14px;font-size:8px;color:var(--white)}
.arrows{position:absolute;right:14px;top:11px;display:flex;gap:3px}
.arrows i{width:20px;height:16px;background:var(--white);display:flex;align-items:center;justify-content:center}

.footer{height:215px;background:var(--footer)}
.footer-col{position:absolute;top:0}
.footer-col h4{font-size:16.5px;font-weight:400;color:#bbb;margin-top:38px}
.footer-brand{margin-top:37px;display:flex;align-items:center;gap:8px;color:var(--white);font-weight:700;font-size:13px}
.footer-col p{font-size:8.5px;line-height:12.5px;color:#888;margin-top:12px;width:206px}
.bullets{list-style:none;margin-top:14px}
.bullets li{font-size:8.5px;color:#888;line-height:19px;display:flex;align-items:center;gap:6px}
.bullets li::before{content:"";width:4px;height:4px;border-radius:50%;background:var(--yellow)}
.contacts{list-style:none;margin-top:15px}
.contacts li{display:flex;gap:8px;font-size:8px;color:#aaa;line-height:10px;margin-bottom:9px}
.contacts em{flex:none;width:16px;height:16px;border-radius:50%;background:var(--yellow);display:flex;align-items:center;justify-content:center}
.form{margin-top:15px;width:132px}
.field{border:1px solid #555;height:20px;font-size:7.5px;color:#888;padding:6px 8px;margin-bottom:6px}
.field.tall{height:40px}
.send{height:20px;background:#3a3a3a;text-align:center;color:var(--yellow);font-size:8px;line-height:20px}
.copyright{height:23px;background:var(--footer-base);text-align:center;font-size:7.5px;color:#888;line-height:23px}
</style>
</head>
<body>
<svg class="board-shade" viewBox="0 0 1200 2347" aria-hidden="true"><polygon points="0,1449 1200,1084 1200,2347 0,2347" fill="var(--board-grey)"/></svg>
<div class="board-title">QUORVANTELLINE LAYOUT</div>

<div class="site">
  <header>
    <div class="topbar"><div class="inner">
      <div class="brand"><span class="brand-mark"></span>QUORVANTELLINE</div>
      <div class="contact-strip">
        <div class="contact-item">
          <div class="contact-icon"><svg width="9" height="9" viewBox="0 0 24 24"><path fill="#f2b91a" d="M6.6 10.8a15 15 0 0 0 6.6 6.6l2.2-2.2c.3-.3.7-.4 1-.2 1.1.4 2.3.6 3.6.6.6 0 1 .4 1 1V20c0 .6-.4 1-1 1A17 17 0 0 1 3 4c0-.6.4-1 1-1h3.5c.6 0 1 .4 1 1 0 1.3.2 2.5.6 3.6.1.3 0 .7-.2 1z"/></svg></div>
          <div><div class="contact-label">Call</div><div class="contact-value">(800) 555 0142</div></div>
        </div>
        <div class="contact-item">
          <div class="contact-icon"><svg width="9" height="7" viewBox="0 0 20 14"><rect width="20" height="14" fill="#f2b91a"/><path d="M0 0l10 8 10-8" fill="none" stroke="#0d2c5e" stroke-width="2"/></svg></div>
          <div><div class="contact-label">Email</div><div class="contact-value">info@quorvantelline.com</div></div>
        </div>
      </div>
    </div></div>
    <nav class="navbar"><div class="inner">
      <ul class="nav-links">
        <li class="active">HOME</li><li>ABOUT US</li><li>SERVICE</li><li>PRODUCT</li><li>CONTACT US</li>
      </ul>
      <div class="social"><span>Vyne</span><span>Plexa</span><span>Chirrup</span><span>Linkwell</span></div>
    </div></nav>
  </header>

  <section class="hero" role="img" aria-label="Dewatering pump discharging groundwater from a construction site pipe">
    <div class="hero-caption"><h1>QUORVANTELLINE</h1><p>We Provide Our best Service</p></div>
    <div class="hero-dots"><span></span><span class="on"></span><span></span></div>
  </section>

  <section class="intro"><div class="inner">
    <h2 class="intro-heading">PLUMBING<br>PROBLEM?<small>We can help you!</small></h2>
    <div class="intro-copy">
      <h2>Professional Plumbing Services</h2>
      <p>Lorem Ipsum is simply dummy text of the printing and typesetting industry. Lorem Ipsum has been the industry's standard dummy text ever since the 1500s, when an unknown printer took a galley</p>
      <span class="btn">CONTACT US</span>
    </div>
  </div></section>

  <section class="services"><div class="inner">
    <h2 class="section-title">OUR SERVICES</h2>
    <div class="service-cards">
      <article class="service-card">
        <div class="service-photo" role="img" aria-label="Workers laying dewatering pipe in an excavated trench" style="background:linear-gradient(160deg,#8a7a5e,#b9a987 60%,#6f6a5c)"></div>
        <h3>CONSTRUCTION DEWATERING</h3>
        <p>Lorem Ipsum is simply dummy text of the printing and typesetting industry.</p>
      </article>
      <article class="service-card">
        <div class="service-photo" role="img" aria-label="Blue centrifugal pump available for rental" style="background:linear-gradient(160deg,#7d6a58,#2e5bb8 50%,#9a8f82)"></div>
        <h3>PUMPS AND EQUIPMENT RENTAL</h3>
        <p>Lorem Ipsum is simply dummy text of the printing and typesetting industry.</p>
      </article>
      <article class="service-card">
        <div class="service-photo" role="img" aria-label="Bypass pumping hoses laid across a work site" style="background:linear-gradient(160deg,#2a2a2a,#8a4a3a 50%,#a79a86)"></div>
        <h3>BYPASS PUMPING</h3>
        <p>Lorem Ipsum is simply dummy text of the printing and typesetting industry.</p>
      </article>
    </div>
  </div></section>

  <section class="products"><div class="inner">
    <h2 class="section-title">OUR PRODUCTS</h2>
    <div class="product-grid">
      <div class="product-tile" role="img" aria-label="Green surface water pump" style="grid-column:1;grid-row:1"></div>
      <div class="product-feature"><div class="product-feature-frame">
        <h3>PRODUCT NAME HERE</h3>
        <p>Lorem Ipsum is simply dummy text of the printing and typesetting industry. Lorem Ipsum has been the.</p>
        <span class="btn">&#128722; BUY NOW</span>
      </div></div>
      <div class="product-tile" role="img" aria-label="Range of submersible borehole pumps" style="grid-column:3;grid-row:1"></div>
      <div class="product-tile" role="img" aria-label="Blue end-suction centrifugal pump" style="grid-column:1;grid-row:2"></div>
      <div class="product-tile" role="img" aria-label="Stainless steel submersible trash pump" style="grid-column:3;grid-row:2"></div>
    </div>
  </div></section>

  <section class="stats"><div class="inner">
    <div class="stat" style="left:124px"><strong>180</strong><span>PROJECTS COMPLETE</span></div>
    <div class="stat" style="left:289px"><strong>175</strong><span>SATISFIED CLIENTS</span></div>
    <div class="stat" style="left:458px"><strong>25</strong><span>ACTIVE EXPERTS</span></div>
    <div class="stat" style="left:624px"><strong>4999</strong><span>DAYS OF WORK</span></div>
  </div></section>

  <section class="trust"><div class="inner">
    <h2 style="left:0">OUR CLIENTS</h2>
    <h2 style="left:386px">TESTIMONIALS</h2>
    <div class="client-grid">
      <div class="client"><i></i>Talvero</div>
      <div class="client"><i></i>Crennick</div>
      <div class="client"><i></i>Osmund &amp; Ray</div>
      <div class="client"><i></i>Pellaro</div>
      <div class="client"><i></i>Vastrin</div>
      <div class="client"><i></i>Dunmere</div>
    </div>
    <div class="testimonial">
      <blockquote><b>&ldquo;</b>Lorem Ipsum is simply dummy text of the printing and typesetting industry. Lorem Ipsum has been the industry's standard dummy text ever since the 1500s, when an unknown printer. ...</blockquote>
      <div class="testimonial-bar">
        <div class="avatar" role="img" aria-label="Customer portrait"></div>
        <span>ARDEL FINCH</span>
        <div class="arrows">
          <i><svg width="6" height="8" viewBox="0 0 6 8"><path d="M5 0L1 4l4 4" fill="none" stroke="#e0a812" stroke-width="1.5"/></svg></i>
          <i><svg width="6" height="8" viewBox="0 0 6 8"><path d="M1 0l4 4-4 4" fill="none" stroke="#e0a812" stroke-width="1.5"/></svg></i>
        </div>
      </div>
    </div>
  </div></section>

  <footer>
    <div class="footer"><div class="inner">
      <div class="footer-col" style="left:0">
        <div class="footer-brand"><span class="brand-mark"></span>QUORVANTELLINE</div>
        <p>Lorem Ipsum is simply dummy text of the printing and typesetting industry. Lorem Ipsum has been the industry's standard dummy text ever since the 1500s, when an unknown printer took a galley of type an</p>
      </div>
      <div class="footer-col" style="left:269px">
        <h4>SERVICE</h4>
        <ul class="bullets"><li>Lorem Ipsum is</li><li>simply dummy</li><li>text of the print-</li><li>ing and typeset</li></ul>
      </div>
      <div class="footer-col" style="left:414px">
        <h4>CONTACT US</h4>
        <ul class="contacts">
          <li><em><svg width="8" height="8" viewBox="0 0 24 24"><path fill="#fff" d="M6.6 10.8a15 15 0 0 0 6.6 6.6l2.2-2.2c.3-.3.7-.4 1-.2 1.1.4 2.3.6 3.6.6.6 0 1 .4 1 1V20c0 .6-.4 1-1 1A17 17 0 0 1 3 4c0-.6.4-1 1-1h3.5c.6 0 1 .4 1 1 0 1.3.2 2.5.6 3.6.1.3 0 .7-.2 1z"/></svg></em><span style="padding-top:3px">Call: (800) 555 0142</span></li>
          <li><em><svg width="8" height="6" viewBox="0 0 20 14"><rect width="20" height="14" fill="#fff"/><path d="M0 0l10 8 10-8" fill="none" stroke="#f2b91a" stroke-width="2"/></svg></em><span style="padding-top:3px">Email: info@quorvantelline.com</span></li>
          <li><em><svg width="7" height="9" viewBox="0 0 12 16"><path fill="#fff" d="M6 0a6 6 0 0 0-6 6c0 4.5 6 10 6 10s6-5.5 6-10a6 6 0 0 0-6-6zm0 8.5A2.5 2.5 0 1 1 6 3.5a2.5 2.5 0 0 1 0 5z"/></svg></em><span style="padding-top:3px">Address: Lorem Ipsum is simply<br>dummy text ,Florida</span></li>
        </ul>
      </div>
      <div class="footer-col" style="left:600px">
        <h4>GET IN TOUCH</h4>
        <div class="form">
          <div class="field">Name:</div>
          <div class="field">Email:</div>
          <div class="field tall">Message:</div>
          <div class="send">SEND</div>
        </div>
      </div>
    </div></div>
    <div class="copyright">&copy; 2018 Quorvantelline. All Rights Reserved.</div>
  </footer>
</div>
</body>
</html>
```